Stationery Design Project Orvik Tal Industries

We need a stationary design that is clean, simple, professional.

You have helped create our business card so we feel that you understand already what we are after. We will help guide you with our feedback as you put forward submissions. We really have no idea how its meant to be done

please submit at least 1 design that has a opaque image/logo/part of word in middle of page, like a water mark?? I don't design letterheads you know best. We are looking forward to seeing your submissions

details on letterhead are

logo and company name
phone number
address
email
website

If there is usually more information that gets put on please let us know what that would be.

Thank you Radek

Sorry to all the designers that have been invited.  This project is for designer Radek. I just put the project through wrong and automatically many were invited.  I apologise again and thank you for your time.

Regards
The Team at Orvik Tal Industries.

```html
<!DOCTYPE html>
<html lang="en">
<head>
<meta charset="utf-8">
<title>Orvik Tal Industries — Stationery</title>
<link href="https://fonts.googleapis.com/css2?family=Barlow:ital,wght@0,400;0,600;0,700;1,400&family=Open+Sans:wght@400;700&display=swap" rel="stylesheet">
<style>
  :root{
    --bg:#e8e8e8;
    --paper:#f7f7f7;
    --orange:#e07a1e;
    --ink:#3a3a3a;
    --grey:#7a7a7a;
    --faint:#e4e4e4;
    --label:#6e6e6e;
  }
  *{box-sizing:border-box;margin:0;padding:0}
  html,body{width:1200px;height:1000px;overflow:hidden;background:var(--bg)}
  body{position:relative;font-family:"Open Sans",sans-serif;color:var(--ink)}

  .sheet{position:absolute;background:var(--paper);box-shadow:0 2px 6px rgba(0,0,0,.12),0 6px 0 -2px #f1f1f1,0 8px 8px -2px rgba(0,0,0,.1);overflow:hidden}
  .rule-top{position:absolute;top:14px;right:0;height:2px;background:var(--orange)}
  .rule-bottom{position:absolute;bottom:14px;left:0;height:2px;background:var(--orange)}

  .brand{position:absolute;display:flex;align-items:center;gap:6px;font-family:"Barlow",sans-serif;font-weight:700;color:var(--grey);text-transform:uppercase;letter-spacing:.04em;white-space:nowrap}
  .brand-dot{width:10px;height:10px;border-radius:50%;background:var(--orange);flex:none}

  .watermark{position:absolute;font-family:"Barlow",sans-serif;font-weight:700;text-transform:uppercase;color:var(--faint);text-align:center;line-height:1;letter-spacing:.04em}

  .contact{position:absolute;text-align:right;font-size:6px;line-height:1.45;color:var(--grey)}
  .contact .name{font-weight:700;color:var(--ink);font-size:6.5px;letter-spacing:.05em}
  .tag{display:inline-block;width:4px;height:4px;background:var(--orange);margin-left:3px;vertical-align:middle}

  .label{position:absolute;font-family:"Barlow",sans-serif;font-style:italic;font-size:20px;color:var(--label)}
  .label::before{content:"*";color:var(--orange);font-style:normal}

  /* Letterhead */
  .letterhead{left:90px;top:40px;width:360px;height:509px}
  .letter-meta{position:absolute;left:28px;top:150px;width:52px;font-size:5.5px;line-height:1.5;color:var(--grey)}
  .letter-meta b{color:var(--ink)}
  .letter-body{position:absolute;left:92px;top:126px;width:240px;font-size:5.6px;line-height:1.65;color:var(--grey)}
  .letter-body h1{font-size:9px;color:var(--ink);text-align:center;margin-bottom:12px}
  .letter-body p{margin-bottom:8px;text-align:justify}
  .signoff{position:absolute;left:92px;top:310px;font-size:5.5px;line-height:1.6;color:var(--grey)}
  .signoff b{color:var(--ink)}

  /* Folder */
  .folder{left:640px;top:40px;width:400px;height:566px}
  .folder-spine{position:absolute;left:0;top:0;bottom:0;width:12px;border-right:1px solid #dedede;background:#f2f2f2}
  .sheet-mail{position:absolute;right:26px;font-size:7px;font-weight:700;color:var(--ink);white-space:nowrap}

  /* Compliment slip */
  .slip{left:40px;top:610px;width:420px;height:200px}
  .slip-note{position:absolute;left:150px;bottom:30px;font-size:7px;font-weight:700;color:var(--grey)}

  /* Envelope */
  .envelope{left:540px;top:660px;width:500px;height:250px}
  .envelope-flap{position:absolute;left:0;right:0;top:70px;height:0;border-top:1px solid #e2e2e2}
</style>
</head>
<body>

  <!-- Letterhead -->
  <section class="sheet letterhead">
    <div class="brand" style="left:22px;top:20px;font-size:13px"><span class="brand-dot"></span>Orvik Tal Industries</div>
    <div class="rule-top" style="width:150px"></div>
    <div class="rule-bottom" style="width:110px"></div>
    <div class="contact" style="right:22px;top:38px">
      <div class="name">NAME SURNAME</div>
      <div>CEO</div>
      <div>5634 New York</div>
      <div>Central Park</div>
      <div style="margin-top:3px">+0435 542 676<span class="tag"></span></div>
      <div>+0435 542 676<span class="tag"></span></div>
      <div>www.yourwebsite.com<span class="tag"></span></div>
      <div>info@yourcompany.com<span class="tag"></span></div>
    </div>
    <div class="letter-meta">
      <b>Date</b><br>14.11.2015<br><br>
      <b>Address</b><br>Jan Novak<br>Main Street 12<br>New York
    </div>
    <div class="letter-body">
      <h1>Lorem ipsum dolor sit amet</h1>
      <p>Lorem ipsum dolor sit amet, consectetur adipiscing elit. Sed do eiusmod tempor incididunt ut labore et dolore magna aliqua. Ut enim ad minim veniam, quis nostrud exercitation ullamco laboris nisi ut aliquip ex ea commodo consequat.</p>
      <p>Lorem ipsum dolor sit amet, consectetur adipiscing elit. Sed do eiusmod tempor incididunt ut labore et dolore magna aliqua. Ut enim ad minim veniam, quis nostrud exercitation ullamco laboris nisi ut aliquip ex ea commodo consequat.</p>
      <p>Lorem ipsum dolor sit amet, consectetur adipiscing elit. Sed do eiusmod tempor incididunt ut labore et dolore magna aliqua. Ut enim ad minim veniam, quis nostrud exercitation ullamco laboris nisi ut aliquip ex ea commodo consequat.</p>
    </div>
    <div class="signoff"><b>With best regards,</b><br>John Doe<br>CEO</div>
    <div class="watermark" style="left:150px;top:380px;width:180px;font-size:26px">Orvik Tal<br>Industries</div>
  </section>
  <div class="label" style="left:470px;top:50px">Letterhead</div>

  <!-- Folder -->
  <section class="sheet folder">
    <div class="folder-spine"></div>
    <div class="brand" style="left:34px;top:24px;font-size:15px"><span class="brand-dot"></span>Orvik Tal Industries</div>
    <div class="rule-top" style="width:130px"></div>
    <div class="rule-bottom" style="left:12px;width:150px"></div>
    <div class="watermark" style="left:50px;top:220px;width:320px;font-size:44px;color:#d6d6d6">Orvik Tal<br>Industries</div>
    <div class="sheet-mail" style="bottom:30px">info@yourcompany.com<span class="tag"></span></div>
  </section>
  <div class="label" style="left:1050px;top:10px">Folder</div>

  <!-- Compliment slip -->
  <section class="sheet slip">
    <div class="brand" style="left:22px;top:22px;font-size:13px"><span class="brand-dot"></span>Orvik Tal Industries</div>
    <div class="rule-top" style="width:160px"></div>
    <div class="rule-bottom" style="width:110px"></div>
    <div class="contact" style="right:22px;top:48px">
      <div class="name">NAME SURNAME</div>
      <div>CEO</div>
      <div>5634 New York</div>
      <div>Central Park</div>
      <div style="margin-top:3px">+0435 542 676<span class="tag"></span></div>
      <div>www.yourwebsite.com<span class="tag"></span></div>
      <div>info@yourcompany.com<span class="tag"></span></div>
    </div>
    <div class="slip-note">With Compliments</div>
  </section>
  <div class="label" style="left:40px;top:840px">Compliment slip</div>

  <!-- Envelope -->
  <section class="sheet envelope">
    <div class="brand" style="left:26px;top:22px;font-size:14px"><span class="brand-dot"></span>Orvik Tal Industries</div>
    <div class="rule-top" style="width:220px"></div>
    <div class="envelope-flap"></div>
    <div class="rule-bottom" style="width:260px"></div>
    <div class="sheet-mail" style="bottom:28px">info@yourcompany.com<span class="tag"></span></div>
  </section>
  <div class="label" style="left:540px;top:930px">Envelope</div>

</body>
</html>
```